Orbell Consulting- executive coaching business

looking for business card design for a newly started coaching business.
specialising in Exective coaching, Leadership, NLP and Motivation.
Looking for a simple, classy design using the existing logo attached and colour themes that complement the logo.
No red or orange in the business card design please.

Target Market(s)

Defence and Veteran community

Industry/Entity Type

Life Coaching

Contact Information for Business Card

looking for business cards for newly started coaching business.
specialising in Exective Coaching, Leadership, NLP and Motivation

Font styles to use
Serif
Script

Colors
0556a4
3176b5
86cfc6
33b8a4

Requirements
Must have
• Logo
• Email address- Jess@orbellconsulting.com.au
• Contact number
• Services provided - Executive Coaching, Leadership, NLP and Motivational Mapping.
Nice to have
• Same colours as logo
Should not have
• Red or orange

```html
<!DOCTYPE html>
<html lang="en">
<head>
<meta charset="utf-8">
<title>Orbell Consulting – Business Cards</title>
<link rel="stylesheet" href="https://fonts.googleapis.com/css2?family=Montserrat:wght@700&family=Open+Sans:wght@400;600&display=swap">
<style>
  :root {
    --stage: #e9e4dc;
    --card-white: #ffffff;
    --brand-blue: #0556a4;
    --mid-blue: #3176b5;
    --card-blue: #1e7fd0;
    --card-blue-dark: #0d63b5;
    --teal: #33b8a4;
    --mint: #86cfc6;
    --text-grey: #8a8a8a;
    --shade: rgba(0,0,0,.18);
  }
  * { box-sizing: border-box; margin: 0; padding: 0; }
  html, body { width: 1200px; height: 1023px; overflow: hidden; }
  body { background: var(--stage); font-family: "Open Sans", Arial, sans-serif; position: relative; }

  .card {
    position: absolute;
    width: 560px; height: 320px;
    border-radius: 4px;
    box-shadow: 0 14px 30px var(--shade);
    overflow: hidden;
  }
  .card--front { left: 110px; top: 110px; background: var(--card-white); }
  .card--back {
    left: 530px; top: 590px;
    background: linear-gradient(160deg, var(--card-blue) 0%, var(--card-blue-dark) 100%);
    color: #fff;
  }

  .decor {
    position: absolute; right: -20px; top: -10px;
    width: 230px; height: 340px;
    border-radius: 40% 60% 50% 50%;
  }
  .card--front .decor { background: radial-gradient(ellipse at center, rgba(0,0,0,.06), rgba(0,0,0,0) 70%); }
  .card--back .decor { background: radial-gradient(ellipse at center, rgba(0,30,80,.18), rgba(0,0,0,0) 70%); }

  .brand { display: flex; align-items: center; gap: 16px; }
  .brand__dot {
    width: 58px; height: 58px; border-radius: 50%;
    border: 2px solid currentColor; flex: none;
  }
  .brand__name {
    font-family: "Montserrat", Arial, sans-serif; font-weight: 700;
    font-size: 34px; letter-spacing: .5px; text-transform: uppercase; line-height: 1;
  }
  .card--front .brand { position: absolute; left: 44px; top: 48px; color: var(--brand-blue); }
  .card--front .brand__dot { color: #b9b9b9; }
  .rule { position: absolute; height: 2px; background: var(--teal); }
  .card--front .rule { left: 118px; top: 122px; width: 360px; }

  .person { position: absolute; left: 44px; top: 156px; display: flex; align-items: baseline; gap: 14px; }
  .person__name { font-family: "Montserrat", Arial, sans-serif; font-weight: 700; font-size: 20px; color: var(--mid-blue); text-transform: uppercase; }
  .person__role { font-weight: 600; font-size: 15px; color: var(--teal); }

  .contacts { position: absolute; left: 44px; top: 200px; list-style: none; font-size: 14px; color: var(--text-grey); line-height: 26px; }
  .contacts li { display: flex; align-items: center; gap: 10px; }
  .icon { width: 14px; height: 14px; fill: var(--teal); flex: none; }

  .address { position: absolute; left: 330px; top: 200px; font-size: 14px; color: var(--text-grey); line-height: 26px; font-style: normal; }

  .card--back .brand { position: absolute; left: 130px; top: 110px; color: #fff; }
  .card--back .rule { background: #fff; left: 130px; width: 330px; height: 2px; }
  .card--back .rule--top { top: 98px; }
  .card--back .rule--bottom { top: 184px; }
  .services { position: absolute; left: 0; right: 0; bottom: 34px; text-align: center; font-size: 15px; letter-spacing: .3px; }
</style>
</head>
<body>
  <section class="card card--front" aria-label="Business card front">
    <div class="decor" role="img" aria-label="Faint tree branch illustration"></div>
    <div class="brand">
      <span class="brand__dot"></span>
      <span class="brand__name">Orbell Consulting</span>
    </div>
    <div class="rule"></div>
    <div class="person">
      <span class="person__name">Daniel Whitford</span>
      <span class="person__role">Director</span>
    </div>
    <ul class="contacts">
      <li><svg class="icon" viewBox="0 0 16 16"><path d="M3 1h3l1.5 4-2 1.3a9 9 0 0 0 4.2 4.2L11 8.5l4 1.5v3a2 2 0 0 1-2 2A12 12 0 0 1 1 3a2 2 0 0 1 2-2z"/></svg>0412 555 018</li>
      <li><svg class="icon" viewBox="0 0 16 16"><path d="M1 3h14v10H1z M1 3l7 6 7-6" fill="none" stroke="#33b8a4" stroke-width="1.6"/></svg>Jess@orbellconsulting.com.au</li>
      <li><svg class="icon" viewBox="0 0 16 16"><circle cx="8" cy="8" r="7"/></svg>www.orbellconsulting.com.au</li>
    </ul>
    <address class="address">Consulting Rooms<br>88 Ridgeline Road<br>Kingsford VIC 3032</address>
  </section>

  <section class="card card--back" aria-label="Business card back">
    <div class="decor" role="img" aria-label="Faint tree branch illustration"></div>
    <div class="rule rule--top"></div>
    <div class="brand">
      <span class="brand__dot"></span>
      <span class="brand__name">Orbell Consulting</span>
    </div>
    <div class="rule rule--bottom"></div>
    <p class="services">Executive Coaching | Leadership | NLP &amp; Motivational</p>
  </section>
</body>
</html>
```